Feral Horizon, a 3d voxel survival video game needs a card for gaming conventions

I am the lead developer for Feral Horizon http://www.FeralHorizon.example and need a business card to hand out at an indie gaming convention
The card would need to include the game name, website url, my name, position (Lead Developer), e-mail and phone number
The game is a 3d, voxel (with smooth terrain) based survival game with guns and wildlife. The main icon of the game would likely be a grizzly bear but I am willing to accept other designs too.
Attached is a media kit for the game with some images you can use but don't have to its just what little art I can provide. Anything on the website or from the video game can also be used. unrelated art can also be used.
Target Market(s)
Indie Developers/publishers at conferences
Industry/Entity Type
Games
Contact Information for Business Card
Name: Corwin Aldersby
Position: Lead Developer
E-mail: Pale_Lanterns@mailbox.example
Phone number: 555-207-3186

```html
<!DOCTYPE html>
<html lang="en">
<head>
<meta charset="utf-8">
<title>Feral Horizon – Business Card</title>
<link href="https://fonts.googleapis.com/css2?family=Open+Sans:wght@400;600;700&display=swap" rel="stylesheet">
<style>
  :root {
    --stage: #e9e6e2;
    --night-top: #1e2a44;
    --night-bottom: #0b0f12;
    --fur-light: #a0764c;
    --fur-dark: #5a3a20;
    --brand-red: #a8321f;
    --ink-light: #ffffff;
    --card-white: #ffffff;
    --shadow: rgba(0,0,0,0.18);
  }
  * { box-sizing: border-box; margin: 0; padding: 0; }
  html, body {
    width: 1200px; height: 900px; overflow: hidden;
    background: var(--stage);
    font-family: "Open Sans", sans-serif;
  }
  .canvas { position: relative; width: 1200px; height: 900px; }

  .card {
    position: absolute;
    box-shadow: 0 6px 18px var(--shadow);
    overflow: hidden;
  }
  .card--front {
    left: 238px; top: 62px; width: 555px; height: 342px;
  }
  .card--back {
    left: 459px; top: 518px; width: 559px; height: 343px;
    background: var(--card-white);
  }

  .front__scene {
    position: absolute; inset: 0;
    background: linear-gradient(160deg, var(--night-top) 0%, #17223a 40%, var(--night-bottom) 100%);
  }
  .front__bear {
    position: absolute; left: 290px; top: 20px; width: 265px; height: 322px;
    border-radius: 48% 40% 0 0 / 30% 26% 0 0;
    background: radial-gradient(ellipse at 40% 35%, var(--fur-light) 0%, #84603c 45%, var(--fur-dark) 100%);
  }

  .brand {
    position: absolute;
    font-weight: 700;
    text-transform: uppercase;
    color: var(--brand-red);
    line-height: 1.05;
  }
  .brand--front {
    left: 44px; top: 40px;
    font-size: 32px; letter-spacing: 2px;
  }
  .brand--back {
    left: 0; right: 0; top: 116px;
    text-align: center;
    font-size: 46px; letter-spacing: 3px;
  }

  .contact { position: absolute; left: 41px; top: 183px; color: var(--ink-light); }
  .contact__name { font-size: 18px; font-weight: 600; }
  .contact__role { font-size: 15px; font-weight: 400; margin-top: -1px; }
  .contact__list { list-style: none; margin-top: 30px; font-size: 14.5px; }
  .contact__item { display: flex; align-items: center; gap: 9px; height: 21px; }
  .contact__icon { width: 11px; height: 11px; fill: var(--ink-light); }
</style>
</head>
<body>
<main class="canvas">

  <section class="card card--front">
    <div class="front__scene" role="img" aria-label="Night forest landscape with dark pine silhouettes under a deep blue sky"></div>
    <div class="front__bear" role="img" aria-label="Photograph of a grizzly bear standing and looking left"></div>

    <div class="brand brand--front">Feral<br>Horizon</div>

    <div class="contact">
      <p class="contact__name">Corwin Aldersby</p>
      <p class="contact__role">Lead Developer</p>
      <ul class="contact__list">
        <li class="contact__item">
          <svg class="contact__icon" viewBox="0 0 24 24" aria-hidden="true"><path d="M6.6 10.8a15.1 15.1 0 0 0 6.6 6.6l2.2-2.2a1 1 0 0 1 1-.25 11.4 11.4 0 0 0 3.6.57 1 1 0 0 1 1 1V20a1 1 0 0 1-1 1A17 17 0 0 1 3 4a1 1 0 0 1 1-1h3.5a1 1 0 0 1 1 1c0 1.25.2 2.45.57 3.57a1 1 0 0 1-.25 1z"/></svg>
          <span>555-207-3186</span>
        </li>
        <li class="contact__item">
          <svg class="contact__icon" viewBox="0 0 24 24" aria-hidden="true"><path d="M2 5h20v14H2z M2 5l10 8 10-8" fill="none" stroke="#fff" stroke-width="0"/><path d="M2 6.5V19h20V6.5l-10 7.5z M3 5h18l-9 6.8z"/></svg>
          <span>Pale_Lanterns@mailbox.example</span>
        </li>
      </ul>
    </div>
  </section>

  <section class="card card--back">
    <div class="brand brand--back">Feral<br>Horizon</div>
  </section>

</main>
</body>
</html>
```